Desserts Business Card Design

I own a dessert business and cakes and cupcakes are my biggest sellers. I have been running this as a part time business since 2007. I am now looking to expand going full time and open a store front within he next 12 months.
With this expansion I am looking to have my own design setup for the business.

I have been using a design on my cards provided to me by a website I got the cards from. I would like a more original design I can use for the cards, the store front and any other advertising I will be doing. I also have a saying on the back of my business card which I would like to be worked in as well.
"Sweets are sweetest, when made by hand"

Target Market(s)

Younger and older families of all ethnic backgrounds

Industry/Entity Type

Advertising

Contact Information for Business Card

Maribel's Sugarcraft Sweets
Dorian Pike
4372 Halloway Crscent
Oshawa, Ontario
L3T 8N4

Logo Text

Logo styles of interest
Emblem Logo
Pictorial/Combination Logo
Wordmark Logo
Lettermark Logo
Requirements
Must have
• "Sweets are sweetest, when made by hand"
Nice to have
• Maribel's Sugarcraft Sweets - This can actually be turned into a logo which is really what I am looking for. Using MSS, converted to a logo? I am really looking to see what you can provide me with.
A cake or cupcake added on the front of the card?
Should not have
• I cannot think of anything right now. I an looking forward to see the imaginations from the design groups

```html
<!DOCTYPE html>
<html lang="en">
<head>
<meta charset="utf-8">
<title>Maribel's Sugarcraft Sweets – Business Card</title>
<link rel="stylesheet" href="https://fonts.googleapis.com/css2?family=Playfair+Display:ital,wght@0,400;1,400;1,600&family=Didact+Gothic&family=Montserrat:wght@600&display=swap">
<style>
  :root {
    --canvas: #ffffff;
    --cocoa-outer: #5c3511;
    --cocoa-inner: #3d2215;
    --cream: #fbd3c3;
    --rose: #f5a8ad;
    --rose-light: #f9c6c4;
    --ink: #2b1a14;
    --ink-soft: #3a2118;
  }
  * { margin: 0; padding: 0; box-sizing: border-box; }
  html, body { width: 1200px; height: 1000px; overflow: hidden; background: var(--canvas); }
  .stage { position: relative; width: 1200px; height: 1000px; }

  .card {
    position: absolute; top: 189px; width: 341px; height: 573px;
    box-shadow: 6px 7px 10px rgba(0,0,0,0.35);
  }
  .card svg.card-art { position: absolute; inset: 0; }
  .card--front { left: 266px; background: var(--cocoa-outer); }
  .card--back { left: 647px; background: var(--rose); }

  .emblem-art { position: absolute; left: 82px; top: 63px; width: 178px; height: 178px; border-radius: 50%;
    background: radial-gradient(circle, var(--rose-light) 0 70%, var(--rose) 71% 100%); }

  .ornament { position: absolute; width: 18px; height: 18px; border-radius: 50%; }
  .card--front .ornament { background: var(--rose); }
  .card--back .ornament { background: var(--ink-soft); width: 16px; height: 16px; }

  .brand-name {
    position: absolute; left: 0; right: 0; top: 298px; text-align: center;
    font-family: "Playfair Display", serif; font-weight: 400; font-style: normal;
    font-size: 44px; line-height: 61px; color: var(--cream);
  }

  .motto {
    position: absolute; left: 18px; right: 14px; top: 80px; text-align: center;
    font-family: "Playfair Display", serif; font-style: italic; font-weight: 600;
    font-size: 24px; line-height: 35px; color: var(--ink-soft);
  }
  .owner {
    position: absolute; left: 54px; top: 202px;
    font-family: "Montserrat", sans-serif; font-weight: 600; font-size: 22px; color: var(--ink);
  }
  .contact-list {
    position: absolute; left: 64px; top: 281px; list-style: none;
    font-family: "Didact Gothic", sans-serif; font-size: 18px; color: var(--ink);
  }
  .contact-list li { line-height: 24px; }
  .contact-list .phone { margin-bottom: 6px; }
  .contact-list .web { margin-top: 5px; }
  .email {
    position: absolute; left: 39px; top: 488px;
    font-family: "Didact Gothic", sans-serif; font-size: 16.5px; color: var(--ink);
  }
</style>
</head>
<body>
<main class="stage">

  <section class="card card--front" aria-label="Card front">
    <svg class="card-art" width="341" height="573" viewBox="0 0 341 573" aria-hidden="true">
      <rect x="16" y="18" width="309" height="538" rx="22" fill="var(--cocoa-inner)"/>
      <rect x="27" y="29" width="287" height="516" rx="16" fill="none" stroke="var(--cream)" stroke-width="1.6" stroke-dasharray="4 3"/>
      <line x1="89" y1="266" x2="256" y2="266" stroke="var(--cream)" stroke-width="1.6" stroke-dasharray="3 3"/>
      <line x1="89" y1="516" x2="252" y2="516" stroke="var(--cream)" stroke-width="1.6" stroke-dasharray="3 3"/>
    </svg>
    <div class="emblem-art" role="img" aria-label="Cupcake illustration on a striped pink medallion"></div>
    <span class="ornament" style="left:58px;top:263px" role="img" aria-label="Small flourish ornament"></span>
    <span class="ornament" style="left:266px;top:263px" role="img" aria-label="Small flourish ornament"></span>
    <h1 class="brand-name">Maribel's<br>Sugarcraft<br>Sweets</h1>
    <span class="ornament" style="left:58px;top:496px" role="img" aria-label="Small flourish ornament"></span>
    <span class="ornament" style="left:266px;top:496px" role="img" aria-label="Small flourish ornament"></span>
  </section>

  <section class="card card--back" aria-label="Card back">
    <svg class="card-art" width="341" height="573" viewBox="0 0 341 573" aria-hidden="true">
      <rect x="15" y="18" width="310" height="538" rx="20" fill="var(--cream)"/>
      <rect x="29" y="29" width="284" height="514" rx="16" fill="none" stroke="var(--ink-soft)" stroke-width="1.6" stroke-dasharray="4 3"/>
      <line x1="57" y1="279" x2="57" y2="418" stroke="var(--rose)" stroke-width="1.2" stroke-dasharray="3 3"/>
    </svg>
    <p class="motto">‘Sweets are sweetest,<br>when made by hand’</p>
    <h2 class="owner">Dorian Pike</h2>
    <span class="ornament" style="left:58px;top:253px" role="img" aria-label="Small flourish ornament"></span>
    <ul class="contact-list">
      <li class="phone">905 555 0148</li>
      <li>4372 Halloway Cr</li>
      <li>Oshawa, Ontario</li>
      <li>L3T8N4</li>
      <li class="web">www.maribelssweets.com</li>
    </ul>
    <span class="ornament" style="left:58px;top:433px" role="img" aria-label="Small flourish ornament"></span>
    <p class="email">sweet.delights@maribelssweets.com</p>
  </section>

</main>
</body>
</html>
```